Fahrzeugbeschriftung für Informationselektronik
Zielgruppe
SAT-Anlagen, Antennenanlagen, Kabelfernsehen
Telekommunikation, Internet, Netzwerktechnik
Radio- und Fernsehtechnik
Alarmanlagen, Videoüberwachung
Elektrokleinreparaturen
Zielgruppe: Hauptsächlich Privatleute
Beratung, Planung, Neuinstallation und hauptsächlich Service und Reparaturen
Aufgabenstellung
auffällig, anders nicht nur Schrift und Logo fertig
WALDEK Informationselektronik
Master Professional

```html
<!DOCTYPE html>
<html lang="de">
<head>
<meta charset="utf-8">
<title>WALDEK Informationselektronik – Fahrzeugbeschriftung</title>
<link rel="stylesheet" href="https://fonts.googleapis.com/css2?family=Roboto:wght@400;500&family=Roboto+Condensed:wght@500&display=swap">
<style>
  :root {
    --stage: #e6eaec;
    --wrap-white: #ffffff;
    --brand-blue: #2b3fae;
    --brand-blue-light: #8e9ad6;
    --name-grey: #7d7f83;
    --ink: #1c1c1c;
    --list-white: #ffffff;
  }
  html, body {
    margin: 0;
    padding: 0;
    width: 1200px;
    height: 889px;
    overflow: hidden;
    background: var(--stage);
  }
  .livery {
    position: relative;
    width: 1200px;
    height: 889px;
  }
  .livery-surface {
    position: absolute;
    inset: 0;
  }
  .address {
    position: absolute;
    left: 188px;
    top: 504px;
    margin: 0;
    font: 400 11px/15px "Roboto", sans-serif;
    color: var(--ink);
    font-style: normal;
  }
  .company-name {
    position: absolute;
    left: 392px;
    top: 418px;
    margin: 0;
    color: var(--name-grey);
    font-family: "Roboto", sans-serif;
    font-weight: 500;
  }
  .company-name-main {
    display: block;
    font-size: 118px;
    line-height: 112px;
  }
  .company-name-sub {
    display: block;
    font-size: 26px;
    line-height: 32px;
    padding-left: 6px;
  }
  .web-address {
    position: absolute;
    left: 615px;
    top: 572px;
    margin: 0;
    font: 500 17px/20px "Roboto", sans-serif;
    color: var(--ink);
  }
  .service-list {
    position: absolute;
    left: 878px;
    top: 328px;
    margin: 0;
    padding: 0;
    list-style: none;
    font: 500 14.5px/19.6px "Roboto Condensed", sans-serif;
    color: var(--list-white);
  }
  .service-list li::before {
    content: "•";
  }
  .service-list .continued {
    padding-left: 6px;
  }
  .service-list .continued::before {
    content: "";
  }
</style>
</head>
<body>
<main class="livery">
  <svg class="livery-surface" width="1200" height="889" viewBox="0 0 1200 889" aria-hidden="true">
    <defs>
      <clipPath id="wrap-clip">
        <rect x="90" y="305" width="1000" height="345" rx="40"/>
      </clipPath>
    </defs>
    <rect class="wrap-white" x="90" y="305" width="1000" height="345" rx="40" fill="var(--wrap-white)"/>
    <g clip-path="url(#wrap-clip)">
      <path class="blue-band-edge" d="M780 300 C 850 420, 880 540, 880 660 L 1100 660 L 1100 300 Z" fill="var(--brand-blue-light)"/>
      <path class="blue-band" d="M806 300 C 872 420, 900 540, 902 660 L 1100 660 L 1100 300 Z" fill="var(--brand-blue)"/>
    </g>
  </svg>

  <address class="address">Kastanienweg 17<br>50999 Talheim</address>

  <h1 class="company-name">
    <span class="company-name-main">waldek</span>
    <span class="company-name-sub">Informationstechnik</span>
  </h1>

  <p class="web-address">www.waldek-info.de</p>

  <ul class="service-list">
    <li>SAT-Anlagen</li>
    <li>Antennenanlagen</li>
    <li>Kabelfernsehen</li>
    <li>Telekommunikation</li>
    <li>Internet</li>
    <li>Netzwerktechnik Radio</li>
    <li class="continued">und Fernsehtechnik</li>
  </ul>
</main>
</body>
</html>
```